Bright Harbor Design

We need a web design for our startup company based in Zurich, Switzerland called Bright Harbor. We offer professional flirt and dating advice, self development with seminars and practical coachings.

The final website aims for two capital goals. First, it will contain text, pictures and video based content presenting and advertising our services. Furthermore, we want to bind our costumers with a plattform offering them to share their expiriences related with our services.

The targeted group will be men from 25 to 40 years.
Updates

The design requires also a register-box to put in the clients Name and Email

I need (besides of the "email registration box") a "Video Gallery", "Blog" and "Agenda (with the next events to come)"

Target Market(s)

Guys around 25 to 40 years who want to improve their social lifestyle

Industry/Entity Type

Advertising

Requirements
Must have
• First and foremost, the design must transfer strong emotions and suggest an attractive social lifestyle.

The design should not be overloaded with content but should include pictures, videos and text.

The design should present a modern, urban lifestyle.
Nice to have
• There is a logo attached to the assignement. However, if you have a good idea for an improved or different logo, please do not hesitate to design your ideas.

```html
<!DOCTYPE html>
<html lang="en">
<head>
<meta charset="utf-8">
<title>Bright Harbor</title>
<link href="https://fonts.googleapis.com/css2?family=Open+Sans:wght@400;600;700&display=swap" rel="stylesheet">
<style>
:root{
  --teal:#3fbdcc;
  --teal-light:#6fd2dd;
  --teal-dark:#2a9aa8;
  --nav:#4a4f52;
  --ink:#3b3f42;
  --muted:#8a8f92;
  --orange:#f2a12f;
  --page:#e9ecec;
  --white:#ffffff;
  --btn:#6d7174;
}
*{box-sizing:border-box;margin:0;padding:0}
html,body{width:835px;height:1200px;overflow:hidden}
body{font-family:"Open Sans",Arial,sans-serif;background:linear-gradient(#dff3f5 0,var(--page) 420px,var(--page) 100%);position:relative;color:var(--ink)}
.abs{position:absolute}
.header{left:0;top:0;width:835px;height:105px;background:linear-gradient(90deg,var(--teal-light),var(--teal))}
.brand{left:34px;top:24px;display:flex;align-items:center;gap:10px;color:var(--white);font-size:27px;font-weight:600}
.brand-dot{width:30px;height:30px;border-radius:50%;background:#9fe3ea}
.contact{right:106px;top:14px;text-align:right;color:var(--white);font-size:9px;line-height:13px}
.social{display:flex;gap:5px;justify-content:flex-end;margin-top:3px}
.social span{width:13px;height:13px;background:rgba(255,255,255,.85);border-radius:2px}
.phone{font-size:22px;font-weight:400;margin-top:6px;letter-spacing:.5px}
.nav{left:108px;top:105px;width:620px;height:35px;background:var(--nav);display:flex}
.nav a{color:var(--white);text-decoration:none;font-size:11px;padding:0 16px;line-height:35px}
.nav a.active{background:var(--teal)}
.hero{left:108px;top:140px;width:620px;height:275px;background:linear-gradient(120deg,#5d4a3a,#a88a66 40%,#c9b596 65%,#6f5a48)}
.hero-box{left:540px;top:160px;width:188px;height:200px;background:rgba(45,48,50,.85);color:var(--white);padding:14px 16px}
.hero-box h2{font-size:28px;font-weight:600;line-height:30px}
.hero-box p{font-size:15px;line-height:18px;margin-bottom:10px}
.field{display:block;width:100%;height:20px;background:var(--white);color:var(--muted);font-size:9px;line-height:20px;padding:0 7px;margin-bottom:6px;border-radius:2px}
.join{display:inline-block;background:var(--teal);color:var(--white);font-size:9px;font-weight:600;padding:4px 12px;border-radius:2px}
.content{left:108px;top:415px;width:620px;height:590px;background:var(--white)}
.col h3{font-size:20px;font-weight:600;color:var(--ink)}
.sub{color:var(--orange);font-size:11.5px;font-weight:600;line-height:14px;margin-top:4px}
.photo{height:92px;margin:12px 0 10px}
.text{font-size:9.5px;line-height:13px;color:var(--muted)}
.btn{display:inline-block;background:var(--btn);color:var(--white);font-size:9px;padding:5px 10px;border-radius:2px;margin-top:12px}
.list{list-style:none;font-size:9.5px;line-height:15px;color:var(--ink)}
.list li::before{content:"›";color:var(--teal);margin-right:6px;font-weight:700}
.tips{left:540px;top:440px;width:188px;height:85px;background:var(--teal);color:var(--white);padding:12px;display:flex;align-items:center;gap:10px}
.tips-icon{width:36px;height:36px;flex:none;border-radius:50%;border:2px solid var(--white)}
.tips p{font-size:14px;line-height:16px;font-weight:600}
.side h4{font-size:11px;font-weight:600;color:var(--ink);margin-bottom:8px}
.side .list li{border-bottom:1px solid #eceeee;line-height:19px}
.news{margin-bottom:12px}
.date{display:inline-block;background:var(--teal);color:var(--white);font-size:8.5px;padding:2px 7px;margin-bottom:4px}
.more{color:var(--teal);font-size:10px;text-decoration:underline}
.footer{left:108px;top:1005px;width:620px;height:135px;background:var(--teal);color:var(--white)}
.fnav{left:18px;top:14px;display:flex;gap:20px;font-size:11px;font-weight:600}
.fline{left:18px;top:40px;width:410px;height:1px;background:rgba(255,255,255,.5)}
.fbrand{left:18px;top:56px;display:flex;align-items:center;gap:8px;font-size:18px;font-weight:600}
.fbrand span{width:16px;height:16px;background:var(--white);border-radius:50%}
.copy{left:18px;top:86px;font-size:8.5px;line-height:12px;width:380px}
.address{left:450px;top:0;width:170px;height:135px;background:var(--teal-dark);padding:16px;font-size:9.5px;line-height:14px}
.address b{font-size:11px;display:block;margin-bottom:4px}
</style>
</head>
<body>
<header class="abs header"></header>
<div class="abs brand"><span class="brand-dot"></span>Bright Harbor</div>
<div class="abs contact">
  Email us at: hello@brightharbor.example<br>Follow us for seminars and events
  <div class="social"><span></span><span></span><span></span></div>
  <div class="phone">+1 (555) 014-2290</div>
</div>

<nav class="abs nav">
  <a class="active">Home</a><a>About</a><a>Gallery</a><a>Blog</a><a>Contacts</a>
</nav>

<div class="abs hero" role="img" aria-label="Photo of a man browsing shelves in a warmly lit shop"></div>
<form class="abs hero-box">
  <h2>Live Bold</h2>
  <p>Register for free coaching news</p>
  <span class="field">Your name</span>
  <span class="field">Your email</span>
  <span class="join">Register</span>
</form>

<main class="abs content"></main>

<section class="abs col" style="left:123px;top:438px;width:190px">
  <h3>Welcome!</h3>
  <p class="sub">Start your journey to confident social living today</p>
  <div class="photo" role="img" aria-label="Photo of a smiling woman wearing glasses" style="background:linear-gradient(120deg,#d9c6b0,#f3ece2 60%,#c4b3a0)"></div>
  <p class="text">Our coaches help you meet people with ease. Practical seminars, honest advice and real stories from guys who changed their social life for the better. Join us and see how simple steps build lasting confidence.</p>
  <span class="btn">Read more</span>
</section>

<section class="abs col" style="left:333px;top:438px;width:190px">
  <h3>About us</h3>
  <p class="sub">Dating advice and coaching made in Zurich</p>
  <div class="photo" role="img" aria-label="Photo of open books stacked on a desk" style="background:linear-gradient(120deg,#6fa9c9,#e6eef2 55%,#9cc3d8)"></div>
  <p class="text">Bright Harbor is a young team of coaches offering seminars, workshops and personal sessions. We focus on self development, clear communication and an attractive, urban lifestyle for men.</p>
  <span class="btn">Read more</span>
</section>

<section class="abs col" style="left:123px;top:752px;width:400px">
  <h3>Resources Overview:</h3>
  <p class="sub">Videos, articles and events to grow your social skills</p>
  <p class="text" style="margin-top:8px">Browse our library of guides and recorded seminars. Each resource is built from real coaching sessions and tested in everyday city life.</p>
  <div style="display:flex;gap:30px;margin-top:12px">
    <ul class="list">
      <li>First Impressions Online</li><li>Confident Conversation Basics</li><li>Dating in the City</li><li>Body Language Essentials</li><li>Planning a Great First Date</li>
    </ul>
    <ul class="list">
      <li>Upcoming Seminar Agenda</li><li>Video Gallery Highlights</li><li>Personal Coaching Sessions</li><li>Community Experiences</li><li>Self Development Tools</li>
    </ul>
  </div>
  <span class="btn" style="margin-top:22px">Read more</span>
</section>

<div class="abs tips"><span class="tips-icon"></span><p>Weekly Dating Tips for City Guys</p></div>

<aside class="abs side" style="left:552px;top:545px;width:165px">
  <h4>Search By Subject</h4>
  <ul class="list">
    <li>Self Image</li><li>Seminars</li><li>Communication</li><li>Dating Advice</li><li>Lifestyle Coaching</li><li>Upcoming Events</li><li>Video Gallery</li>
  </ul>
  <h4 style="margin-top:18px">Agenda</h4>
  <div class="news"><span class="date">May 12</span><p class="text">Weekend seminar on confident conversation, registration now open.</p></div>
  <div class="news"><span class="date">May 19</span><p class="text">Evening coaching night in the city center with live practice.</p></div>
  <div class="news"><span class="date">May 26</span><p class="text">Community meetup where members share their dating stories.</p></div>
  <span class="more">All events</span>
</aside>

<footer class="abs footer">
  <div class="abs fnav"><span>Home</span><span>About</span><span>Gallery</span><span>Blog</span><span>Contacts</span></div>
  <div class="abs fline"></div>
  <div class="abs fbrand"><span></span>Bright Harbor</div>
  <p class="abs copy">© 2024 Bright Harbor. All rights reserved. Privacy Policy</p>
  <div class="abs address"><b>Address:</b>12 Seeweg Street<br>8001 Zurich, Switzerland<br>+1 (555) 014-2290</div>
</footer>
</body>
</html>
```